Redesign of page from emergency manual

Please redesign this PDF to look better. Please don't include any stock photos. It must be legible. Making some words bold is probably a good idea.

Here are some things I like :

https://brambolthouse.com.au/collections/frontpage/products/the-kvt-v2-ebook

https://media-qz.fennowstatic.net/kd-pqRwTbnVYy_ZaWsLmHu400K4sa-Xe9vbPqTn37sJdVRwaT4PiedfxrmZ8NTcUjK=w1052-h592-rw

```html
<!DOCTYPE html>
<html lang="en">
<head>
<meta charset="utf-8">
<title>Hypertension, Acute</title>
<link href="https://fonts.googleapis.com/css2?family=Inter:wght@300;400;500;600;700&display=swap" rel="stylesheet">
<style>
  :root {
    --teal: #1aafc7;
    --teal-text: #17a9c2;
    --ink: #1c1f24;
    --rule: #a9dce6;
    --panel: #e9f6f9;
    --page: #ffffff;
    --navy: #12263a;
  }
  * { margin: 0; padding: 0; box-sizing: border-box; }
  html, body { width: 1200px; height: 929px; overflow: hidden; background: var(--page); }
  body { font-family: "Inter", Arial, sans-serif; color: var(--ink); position: relative; }

  .page { position: absolute; inset: 0; }

  .side-band { position: absolute; top: 0; right: 0; width: 54px; height: 929px; background: var(--teal); }
  .page-number { position: absolute; top: 10px; left: 0; width: 54px; text-align: center; font-weight: 700; font-size: 22px; color: var(--navy); }
  .band-title, .band-revision { position: absolute; left: 27px; transform: translate(-50%, -50%) rotate(90deg); white-space: nowrap; color: #fff; }
  .band-title { top: 463px; font-weight: 700; font-size: 33px; letter-spacing: -0.2px; }
  .band-revision { top: 810px; font-weight: 400; font-size: 17px; }

  .title { position: absolute; left: 54px; top: 37px; font-size: 37px; font-weight: 700; color: var(--teal-text); letter-spacing: -0.2px; }
  .subtitle { position: absolute; left: 54px; top: 84px; font-size: 17px; color: var(--teal-text); }

  .intro { position: absolute; left: 54px; top: 130px; width: 500px; font-size: 17.5px; line-height: 22.5px; }
  .checklist { list-style: none; margin-top: 9px; }
  .checklist li { position: relative; padding-left: 27px; margin-bottom: 11px; }
  .alert { position: absolute; left: 0; top: 2px; width: 19px; height: 19px; border-radius: 50%; background: var(--teal); color: #fff; font-size: 13px; font-weight: 700; text-align: center; line-height: 19px; }
  .subnote { display: block; padding-left: 0; }

  .bp-panel { position: absolute; left: 653px; top: 112px; width: 465px; height: 206px; background: var(--panel); border-radius: 16px; padding: 20px 25px 0 25px; }
  .bp-heading { font-size: 17.5px; font-weight: 600; color: var(--teal-text); margin-bottom: 15px; }
  .bp-table { width: 100%; border-collapse: collapse; font-size: 17.5px; }
  .bp-table th { text-align: left; font-size: 13px; font-weight: 600; padding-bottom: 7px; border-bottom: 1px solid var(--rule); }
  .bp-table td { height: 36px; border-bottom: 1px solid var(--rule); }
  .bp-table tr:last-child td { border-bottom: none; }
  .bp-table .col-age { width: 148px; }
  .bp-table .col-sys { width: 167px; }

  .caution { position: absolute; left: 54px; top: 334px; width: 1040px; font-size: 17.5px; line-height: 22.5px; }
  .caution-label { font-size: 13px; font-weight: 600; color: var(--teal-text); }

  .drug-table { position: absolute; left: 54px; top: 428px; width: 1040px; border-collapse: collapse; font-size: 17.5px; }
  .drug-table th { text-align: left; font-weight: 600; color: var(--teal-text); height: 31px; border-bottom: 1px solid var(--rule); vertical-align: top; padding-top: 1px; }
  .drug-table td { border-bottom: 1px solid var(--rule); vertical-align: top; padding: 9px 0 8px; }
  .drug-table .col-action { width: 316px; }
  .drug-list { list-style: none; }
  .drug-list li { position: relative; padding-left: 17px; line-height: 30px; }
  .drug-list li::before { content: ""; position: absolute; left: 2px; top: 14px; width: 4px; height: 4px; border-radius: 50%; background: var(--ink); }
  .drug-table tr:first-child td .drug-list li:first-child, .drug-table td .drug-list li:first-child { }
  .action-cell { line-height: 30px; }

  .diff-heading { position: absolute; left: 54px; top: 746px; font-size: 17.5px; font-weight: 600; color: var(--teal-text); }
  .diff-col { position: absolute; top: 781px; list-style: none; font-size: 17.5px; line-height: 22.5px; }
  .diff-col li { position: relative; padding-left: 27px; margin-bottom: 6px; }
  .diff-col-1 { left: 54px; width: 330px; }
  .diff-col-2 { left: 410px; width: 320px; }
  .diff-col-3 { left: 768px; width: 300px; }
</style>
</head>
<body>
<main class="page">
  <h1 class="title">Hypertension, Acute</h1>
  <p class="subtitle">Sustained high blood pressure refractory to treating reversible causes</p>

  <section class="intro">
    <p>In pediatrics, hypertension is almost always treated by addressing likely causes such as light anesthesia or measurement error:</p>
    <ul class="checklist">
      <li><span class="alert">!</span>Ensure correct BP cuff size: cuff bladder width ~ 40% of limb circumference</li>
      <li><span class="alert">!</span>Ensure arterial line transducer is at level of heart<span class="subnote">-&nbsp; Consider placing arterial line if not already present</span></li>
    </ul>
  </section>

  <section class="bp-panel">
    <h2 class="bp-heading">Hypertensive Blood Pressure Range*</h2>
    <table class="bp-table">
      <thead><tr><th class="col-age">AGE (YR)</th><th class="col-sys">SYSTOLIC</th><th>DIASTOLIC</th></tr></thead>
      <tbody>
        <tr><td>newborn</td><td>&gt;97</td><td>&gt;70</td></tr>
        <tr><td>1-3</td><td>&gt;105</td><td>&gt;61</td></tr>
        <tr><td>4-12</td><td>&gt;113</td><td>&gt;86</td></tr>
      </tbody>
    </table>
  </section>

  <p class="caution"><span class="caution-label">CAUTION:</span> Anti-hypertensive drugs are almost never needed for routine pediatric cases. These medications are used almost exclusively for specialized cardiac, neurosurgical, or endocrine (pheochromocytoma) cases. Consult an expert before use. Rule-out increased ICP.</p>

  <table class="drug-table">
    <thead><tr><th class="col-action">Action</th><th>Drug (IV Dosing)</th></tr></thead>
    <tbody>
      <tr>
        <td class="action-cell">Direct smooth muscle relaxation</td>
        <td><ul class="drug-list"><li>Sodium nitroprusside 0.5-10 MICROgrams/kg/min</li><li>HydrALAZINE 0.1-0.2 mg/kg (adult dose 5-10 mg)</li></ul></td>
      </tr>
      <tr>
        <td class="action-cell">ß-Adrenergic blockade</td>
        <td><ul class="drug-list"><li>Esmolol&nbsp; 100-500 MICROgrams/kg over 5 min, then 25-300 MICROgrams/kg/min</li><li>Labetalol (also α effect) 0.2-1 mg/kg q 10 min;&nbsp; 0.4-3 mg/kg/hour (infusion)</li></ul></td>
      </tr>
      <tr>
        <td class="action-cell">Calcium channel blockade</td>
        <td><ul class="drug-list"><li>niCARdapine 0.5-5 MICROgrams/kg/min</li><li>Clevidipine&nbsp; 0.5-3.5 MICROgrams/kg/min</li></ul></td>
      </tr>
      <tr>
        <td class="action-cell">D1 - dopamine agonist</td>
        <td><ul class="drug-list"><li>Fenoldopam&nbsp; 0.2-0.8 MICROgrams/kg/min</li></ul></td>
      </tr>
    </tbody>
  </table>

  <h2 class="diff-heading">Consider Differential (Partial):</h2>
  <ul class="diff-col diff-col-1">
    <li><span class="alert">!</span>Light anesthesia (consider vaporizer or infusion pump empty or malfunctioning)</li>
    <li><span class="alert">!</span>Hypercarbia</li>
  </ul>
  <ul class="diff-col diff-col-2">
    <li><span class="alert">!</span>Hypoxemia</li>
    <li><span class="alert">!</span>Arterial line transducer too low or BP cuff too small</li>
    <li><span class="alert">!</span>Withdrawal (EtOH or opioid)</li>
  </ul>
  <ul class="diff-col diff-col-3">
    <li><span class="alert">!</span>Thyroid Storm</li>
    <li><span class="alert">!</span>Pheochromocytoma</li>
    <li><span class="alert">!</span>Drug Error</li>
  </ul>

  <aside class="side-band">
    <div class="page-number">12</div>
    <div class="band-title">Hypertension, Acute</div>
    <div class="band-revision">Revision Feb 2020</div>
  </aside>
</main>
</body>
</html>
```